New Office Poster Designs

Attached you will find 3 poster designs that we found online along with our logos. Please use our logos to reference any type of color or design.
These posters will be hung around our Loan Offices.

INSTRUCTIONS: Please mimic all 3 posters (MINUS THE SMALL WRITING ON THEM THAT IS NOT IN ENGLISH IGNORE THAT)
but use our logos and colors. Also, if you can make them in Spanish as well as English that is a plus. We will also need 1 additional poster with the below wording.

Additional Poster:
Stuck in a Title Loan? Let us pay it off up to $10,000

Target Market(s)

People looking to get a loan and need money

Industry/Entity Type

Loan Industry - Consumer Lending - Fast easy loans

Requirements
Nice to have
• English and Spanish

```html
<!DOCTYPE html>
<html lang="en">
<head>
<meta charset="utf-8">
<title>Title Loan Payoff Poster</title>
<link rel="stylesheet" href="https://fonts.googleapis.com/css2?family=Archivo+Black&display=swap">
<style>
  :root {
    --page-bg: #ffffff;
    --poster-bg: #ececec;
    --brand-green: #1f5a2c;
    --brand-red: #d7262b;
    --brand-brown: #8a4a26;
  }
  * { margin: 0; padding: 0; box-sizing: border-box; }
  html, body {
    width: 1200px;
    height: 3000px;
    overflow: hidden;
    background: var(--page-bg);
  }
  .poster {
    position: absolute;
    left: 0;
    top: 726px;
    width: 1200px;
    height: 1548px;
    background: var(--poster-bg);
    overflow: hidden;
    font-family: "Archivo Black", "Arial Black", sans-serif;
  }
  .brand {
    position: absolute;
    right: 58px;
    top: 92px;
    text-align: right;
    color: var(--brand-green);
  }
  .brand-name {
    font-size: 66px;
    line-height: 1;
    letter-spacing: 1px;
  }
  .brand-tagline {
    margin-top: 10px;
    font-size: 17px;
    letter-spacing: 4px;
  }
  .rigging {
    position: absolute;
    inset: 0;
  }
  .illustration {
    position: absolute;
  }
  .illustration-man {
    left: 86px; top: 444px; width: 354px; height: 709px;
    background: linear-gradient(180deg, var(--brand-brown) 0%, #b5523a 55%, var(--brand-red) 100%);
    opacity: 0.35;
  }
  .illustration-moneybag {
    left: 820px; top: 1040px; width: 290px; height: 320px;
    background: linear-gradient(160deg, var(--brand-red) 0%, #a8553a 60%, var(--brand-green) 100%);
    opacity: 0.35;
  }
  .illustration-coins {
    left: 700px; top: 1250px; width: 420px; height: 270px;
    background: linear-gradient(160deg, var(--brand-red) 0%, #a8553a 55%, var(--brand-green) 100%);
    opacity: 0.35;
  }
  .step {
    position: absolute;
    height: 76px;
    background: linear-gradient(90deg, var(--brand-red), var(--brand-brown) 55%, var(--brand-green));
    opacity: 0.75;
  }
  .step-top    { left: 201px; top: 1195px; width: 200px; }
  .step-middle { left: 156px; top: 1292px; width: 284px; }
  .step-bottom { left: 93px;  top: 1382px; width: 389px; }

  /* Text set along the rope; origin sits on the pulley */
  .headline-block {
    position: absolute;
    left: 337px;
    top: 58px;
    width: 0;
    height: 0;
    transform: rotate(58.3deg);
    transform-origin: 0 0;
  }
  .headline-block > * {
    position: absolute;
    white-space: nowrap;
    line-height: 1;
    background: linear-gradient(90deg, var(--brand-green) 0%, var(--brand-brown) 60%, var(--brand-red) 100%);
    -webkit-background-clip: text;
    background-clip: text;
    color: transparent;
  }
  .kicker       { left: 542px; top: -181px; font-size: 40px; }
  .headline     { left: 264px; top: -123px; font-size: 110px; }
  .offer-lead   { left: 646px; top: 66px;   font-size: 24px; }
  .offer-amount { left: 505px; top: 99px;   font-size: 72px; }
</style>
</head>
<body>
  <main class="poster">
    <svg class="rigging" width="1200" height="1548" viewBox="0 0 1200 1548" aria-hidden="true">
      <defs>
        <linearGradient id="rope-long" x1="337" y1="58" x2="942" y2="1038" gradientUnits="userSpaceOnUse">
          <stop offset="0" stop-color="#d7262b"/>
          <stop offset="0.5" stop-color="#1f5a2c"/>
          <stop offset="1" stop-color="#d7262b"/>
        </linearGradient>
      </defs>
      <line x1="318" y1="80" x2="296" y2="446" stroke="#a9372c" stroke-width="9" stroke-linecap="round"/>
      <line x1="355" y1="87" x2="942" y2="1038" stroke="url(#rope-long)" stroke-width="7" stroke-linecap="round"/>
      <circle cx="337" cy="58" r="34" fill="none" stroke="var(--brand-red)" stroke-width="7"/>
      <circle cx="337" cy="58" r="8" fill="var(--brand-red)"/>
    </svg>

    <div class="illustration illustration-man" role="img" aria-label="Sketch of a businessman with a briefcase hanging upside down by one foot from the rope"></div>
    <div class="illustration illustration-moneybag" role="img" aria-label="Sketch of a money bag with a dollar sign tied to the rope"></div>
    <div class="illustration illustration-coins" role="img" aria-label="Sketch of a stack of coins with hatched ground beneath"></div>

    <div class="step step-top" role="img" aria-label="Hand-hatched step of a staircase"></div>
    <div class="step step-middle" role="img" aria-label="Hand-hatched step of a staircase"></div>
    <div class="step step-bottom" role="img" aria-label="Hand-hatched step of a staircase"></div>

    <div class="brand">
      <div class="brand-name">Crestline</div>
      <div class="brand-tagline">LOANS – PRESTAMOS</div>
    </div>

    <div class="headline-block">
      <p class="kicker">STUCK IN A</p>
      <h1 class="headline">TITLE LOAN?</h1>
      <p class="offer-lead">LET US PAY IT OFF</p>
      <p class="offer-amount">UP TO $10,000</p>
    </div>
  </main>
</body>
</html>
```